New business card for civil engineering company - "Keystone Audit"

We need a business card designed for our new structural engineering company.

The company name is "Keystone Audit" logo files attached.

We would like the following:
* Two-sided card
* Simple design

Information to be placed on the card:
Name - Marcus Dellow
Job Title - Director / Structural Engineer
Credentials - BEng(Hons), CPEng, CMengNZ, IntPE(NZ)
Email - marcus.dellow@keystoneaudit.co.nz
mobile - 0219364058
website - www.keystoneaudit.co.nz

```html
<!DOCTYPE html>
<html lang="en">
<head>
<meta charset="utf-8">
<title>Keystone Audit – Business Card</title>
<link rel="stylesheet" href="https://fonts.googleapis.com/css2?family=Open+Sans:wght@400;600;700&display=swap">
<style>
  :root {
    --backdrop: #2b2c2e;
    --card-white: #ffffff;
    --card-navy: #2c5078;
    --accent-blue: #3a87c8;
    --rule-blue: #a9cbe8;
    --text-grey: #6e6e6e;
    --wordmark-grey: #3d3d3f;
    --text-light: #ffffff;
  }
  html, body {
    margin: 0;
    padding: 0;
    width: 1200px;
    height: 1200px;
    overflow: hidden;
    background: var(--backdrop);
    font-family: "Open Sans", Arial, sans-serif;
  }
  .canvas {
    position: relative;
    width: 1200px;
    height: 1200px;
  }
  .card {
    position: absolute;
    left: 259px;
    width: 682px;
    height: 389px;
    border-radius: 19px;
    overflow: hidden;
  }
  .card--front { top: 182px; background: var(--card-white); }
  .card--back  { top: 635px; background: var(--card-navy); }

  .front__wordmark {
    position: absolute;
    right: 31px;
    top: 150px;
    margin: 0;
    font-size: 24px;
    font-weight: 600;
    letter-spacing: 1.5px;
    text-transform: uppercase;
    color: var(--wordmark-grey);
  }
  .front__name {
    position: absolute;
    left: 29px;
    top: 190px;
    margin: 0;
    font-size: 24px;
    font-weight: 700;
    color: var(--accent-blue);
  }
  .front__rule {
    position: absolute;
    left: 29px;
    right: 31px;
    top: 222px;
    height: 2px;
    background: var(--rule-blue);
  }
  .front__role {
    position: absolute;
    left: 29px;
    top: 230px;
    margin: 0;
    font-size: 18px;
    line-height: 24px;
    color: var(--text-grey);
  }
  .front__contacts {
    position: absolute;
    left: 29px;
    top: 320px;
    margin: 0;
    padding: 0;
    list-style: none;
    font-size: 17px;
    line-height: 23px;
    color: var(--text-grey);
  }
  .contact {
    display: flex;
    align-items: center;
    gap: 10px;
  }
  .contact__icon {
    width: 18px;
    height: 16px;
    fill: var(--accent-blue);
    flex: none;
  }
  .front__web {
    position: absolute;
    right: 31px;
    top: 343px;
    margin: 0;
    font-size: 17px;
    line-height: 23px;
    color: var(--accent-blue);
  }

  .back__wordmark {
    position: absolute;
    left: 0;
    right: 0;
    top: 258px;
    margin: 0;
    text-align: center;
    font-size: 27px;
    font-weight: 600;
    letter-spacing: 1.5px;
    text-transform: uppercase;
    color: var(--text-light);
  }
  .back__web {
    position: absolute;
    left: 0;
    right: 0;
    top: 344px;
    margin: 0;
    text-align: center;
    font-size: 17px;
    color: var(--text-light);
  }
</style>
</head>
<body>
<main class="canvas">
  <section class="card card--front" aria-label="Card front">
    <p class="front__wordmark">Keystone Audit</p>
    <h1 class="front__name">Marcus Dellow</h1>
    <div class="front__rule"></div>
    <p class="front__role">Director / Structural Engineer<br>BEng(Hons), CPEng, CMengNZ, IntPE(NZ)</p>
    <ul class="front__contacts">
      <li class="contact">
        <svg class="contact__icon" viewBox="0 0 18 16" aria-hidden="true">
          <path d="M5 0h8a1.5 1.5 0 0 1 1.5 1.5v13A1.5 1.5 0 0 1 13 16H5a1.5 1.5 0 0 1-1.5-1.5v-13A1.5 1.5 0 0 1 5 0zm0.5 2v10.5h7V2zM9 13.3a0.9 0.9 0 1 0 0 1.8a0.9 0.9 0 0 0 0-1.8z"/>
        </svg>
        <span>0219364058</span>
      </li>
      <li class="contact">
        <svg class="contact__icon" viewBox="0 0 18 16" aria-hidden="true">
          <path d="M0 3h18v10H0zM1.5 4.2v0.4L9 9.3l7.5-4.7v-0.4zM1.5 6.3v5.5h15V6.3L9 11z"/>
        </svg>
        <span>marcus.dellow@keystoneaudit.co.nz</span>
      </li>
    </ul>
    <p class="front__web">www.keystoneaudit.co.nz</p>
  </section>

  <section class="card card--back" aria-label="Card back">
    <p class="back__wordmark">Keystone Audit</p>
    <p class="back__web">www.keystoneaudit.co.nz</p>
  </section>
</main>
</body>
</html>
```